New Dental Office Needs an Attractive and user friendly Website Designed

I need a website for a new dental office. The Name is Maplecrest Dentistry. I would like a Modern design with a user friendly interface and usability.
I would like a landing page, a page that lists the services we offer: Cosmetic Dentistry, Implants, Dental Hygiene, Emergency Services, Restorations, Dentures
Target Market(s)
Mid to upper class
Industry/Entity Type
Dentistry
Coding
Coded - Design and coding required
Number of Pages Required
1 page
Requirements
Must have
- Landing page that has a scheduling option, Procedures, operating hours, and contact us info
Nice to have
- Appealing design, Soft comforting colors. Easy to navigate page, Modern and professional.

```html
<!DOCTYPE html>
<html lang="en">
<head>
<meta charset="utf-8">
<title>Maplecrest Dentistry</title>
<link href="https://fonts.googleapis.com/css2?family=Inter:wght@300;400;500;600;700;800&display=swap" rel="stylesheet">
<style>
:root{
  --blue:#1c6ff0;
  --blue-dark:#0f55d6;
  --blue-soft:#e9f2ff;
  --green:#1fbf9b;
  --green-dark:#12a384;
  --navy:#0e1a3a;
  --text:#4b5670;
  --muted:#8a93a8;
  --line:#e6ebf3;
  --white:#ffffff;
}
*{box-sizing:border-box;margin:0;padding:0}
html,body{width:1200px;height:4914px;overflow:hidden}
body{position:relative;font-family:"Inter",sans-serif;color:var(--navy);background:var(--white)}
.abs{position:absolute}
.hero-bg{left:0;top:0;width:1200px;height:745px;background:linear-gradient(120deg,#2a7bf5 0%,#1463e6 100%)}
.hero-wave{left:0;top:560px;width:1200px;height:190px}
.topbar{left:0;top:0;width:1200px;height:36px;color:#fff;font-size:10px;display:flex;align-items:center;padding:0 93px}
.topbar .item{display:flex;align-items:center;gap:8px;margin-right:30px}
.topbar .ic{width:20px;height:20px;border-radius:50%;background:#fff;display:flex;align-items:center;justify-content:center}
.topbar .follow{margin-left:auto;display:flex;align-items:center;gap:8px}
.dot-soc{width:20px;height:20px;border-radius:50%;background:rgba(255,255,255,.25)}
.nav{left:78px;top:38px;width:1044px;height:74px;background:#fff;border-radius:10px;display:flex;align-items:center;padding:0 16px;box-shadow:0 6px 20px rgba(10,40,120,.15)}
.brand{font-size:22px;font-weight:700;color:var(--navy);display:flex;align-items:center;gap:8px}
.brand .sq{width:12px;height:12px;background:var(--green);border-radius:3px}
.nav ul{list-style:none;display:flex;gap:44px;margin-left:auto;margin-right:38px;font-size:10px;color:var(--text);letter-spacing:.3px}
.nav li.active{color:var(--green);font-weight:600;border-bottom:2px solid var(--green);padding-bottom:4px}
.btn{display:inline-flex;align-items:center;justify-content:space-between;gap:12px;font-weight:600;font-size:12px;border-radius:6px;padding:0 6px 0 16px}
.btn .bi{width:30px;height:30px;border-radius:5px;background:#fff;display:flex;align-items:center;justify-content:center}
.btn-green{background:var(--green);color:#fff;height:40px}
.btn-blue{background:var(--blue);color:#fff;height:42px;box-shadow:0 6px 14px rgba(28,111,240,.3)}
.btn-white{background:#fff;color:var(--navy);height:42px}
.btn-white .bi{background:var(--green)}
.pill{left:93px;top:183px;background:#fff;color:var(--blue);font-size:9px;font-weight:600;padding:6px 20px;border-radius:20px}
.hero-h1{left:93px;top:222px;color:#fff;line-height:1.1}
.hero-h1 .l1{font-size:52px;font-weight:300;display:block}
.hero-h1 .l2{font-size:58px;font-weight:800;display:block;letter-spacing:.5px}
.hero-p{left:93px;top:368px;width:480px;color:#eaf2ff;font-size:12.5px;line-height:1.6}
.ph{background:linear-gradient(135deg,#cfe0f7,#9fbfe8)}
.hero-img{left:626px;top:156px;width:366px;height:394px;border-radius:32px;background:linear-gradient(135deg,#e8d8cf,#8fb2e6 70%,#3f6fd0)}
.badge-9k{left:682px;top:183px;display:flex;align-items:center}
.av{width:34px;height:34px;border-radius:50%;border:2px solid #fff;background:linear-gradient(135deg,#f0d2c2,#c49e88);margin-right:-10px}
.k9{width:46px;height:46px;border-radius:50%;background:var(--blue);color:#fff;font-weight:700;font-size:14px;display:flex;align-items:center;justify-content:center;border:3px solid #fff;margin-left:6px}
.award{left:992px;top:440px;width:120px;height:120px;border-radius:50%;background:var(--blue);border:2px dashed rgba(255,255,255,.5)}
.info-card{left:193px;top:601px;width:818px;height:110px;background:#fff;border-radius:16px;box-shadow:0 10px 30px rgba(14,40,110,.12);display:flex;align-items:center;padding:0 30px}
.info{display:flex;align-items:center;gap:16px;flex:1;border-right:1px solid var(--line);padding-left:10px}
.info:last-child{border:none}
.info .ib{width:42px;height:42px;border-radius:8px;background:var(--green);display:flex;align-items:center;justify-content:center}
.info small{display:block;font-size:10px;color:var(--text);margin-bottom:3px}
.info strong{font-size:15px;color:var(--blue);font-weight:700}
.info span{font-size:11px;color:var(--navy);line-height:1.4}
.info span b{color:var(--blue)}
.about-img{left:149px;top:858px;width:310px;height:310px;border-radius:50%;background:linear-gradient(135deg,#dbe8f8,#a9c4ea)}
.about-glow{left:110px;top:780px;width:420px;height:420px;border-radius:50%;background:radial-gradient(circle,#eef4ff 0%,rgba(255,255,255,0) 70%)}
.tooth{border-radius:45% 45% 40% 40%;background:linear-gradient(160deg,#ffffff,#cfe0f5)}
.about-tag{left:345px;top:1090px;width:165px;height:82px;background:#fff;border-radius:10px;box-shadow:0 6px 20px rgba(14,40,110,.1);padding:12px}
.about-tag .nm{font-size:14px;font-weight:700}
.about-tag .row{display:flex;align-items:center;margin-top:10px;font-size:9px;color:var(--text)}
.about-tag .av{width:22px;height:22px;border-width:1.5px}
.about-text{left:616px;top:872px;width:470px}
.about-text h2{font-size:30px;line-height:1.3;font-weight:700}
.about-text .sub{color:var(--green);font-size:18px;font-weight:600;margin:14px 0 28px}
.leaf{width:18px;height:18px;border-radius:50%;background:var(--navy);display:block}
.sec-head{left:0;width:1200px;text-align:center}
.sec-head .leaf{margin:0 auto 14px}
.sec-head h2{font-size:40px;font-weight:700;line-height:1.25}
.g{color:var(--green)}
.svc{top:1479px;width:223px;height:330px;background:#fff;border-radius:14px;box-shadow:0 8px 24px rgba(14,40,110,.09);padding:10px}
.svc .im{height:155px;border-radius:12px}
.svc .ico{position:absolute;left:22px;top:130px;width:48px;height:48px;border-radius:8px;background:var(--green);border:3px solid #fff;display:flex;align-items:center;justify-content:center}
.svc .ico.b{background:var(--blue)}
.svc h3{font-size:16px;font-weight:700;margin:44px 8px 10px}
.svc p{font-size:11px;line-height:1.6;color:var(--text);margin:0 8px}
.svc .arr{position:absolute;right:16px;bottom:14px;width:40px;height:40px;border-radius:8px;background:#e2f7f1;display:flex;align-items:center;justify-content:center}
.svc .arr.on{background:var(--blue)}
.dots{left:0;width:1200px;display:flex;justify-content:center;gap:8px}
.dots .c{width:22px;height:14px;border-radius:8px;background:#eef1f6}
.dots .p{width:40px;height:14px;border-radius:8px;background:var(--green)}
.why-head{left:139px;top:1980px}
.why-head h2{font-size:40px;font-weight:700;line-height:1.25;margin-top:12px}
.why-a{left:145px;top:2212px;width:210px;height:183px;border-radius:12px;background:linear-gradient(135deg,#f4e1d8,#e7b4a6);box-shadow:0 8px 24px rgba(14,40,110,.12)}
.why-b{left:330px;top:2160px;width:235px;height:288px;border-radius:16px;background:linear-gradient(135deg,#e6d6cf,#6f93cf)}
.feat{left:622px;width:437px;height:84px;background:#fff;border-radius:10px;box-shadow:0 6px 20px rgba(14,40,110,.08);display:flex;align-items:center;gap:20px;padding:0 10px}
.feat .fi{width:66px;height:66px;border-radius:8px;background:#e4f7f2;display:flex;align-items:center;justify-content:center;flex:none}
.feat .fi.b{background:var(--blue)}
.feat h4{font-size:15px;font-weight:700;margin-bottom:6px}
.feat p{font-size:10.5px;color:var(--text);line-height:1.5}
.slider{left:0;top:2700px;width:1200px;height:308px;overflow:hidden}
.slide{position:absolute;top:0;height:308px;border-radius:12px;overflow:hidden}
.slide.side{background:linear-gradient(135deg,#2a7bf5,#1a62e0)}
.slide.main{left:223px;width:720px;background:linear-gradient(120deg,#2f7ff6,#1661e4);box-shadow:0 10px 30px rgba(14,70,200,.25)}
.ba{position:absolute;left:6px;top:6px;width:242px;height:296px;border-radius:8px;background:linear-gradient(180deg,#f3ece8,#d9c4bc)}
.ba i{position:absolute;left:0;top:147px;width:100%;height:3px;background:#fff}
.tagsm{position:absolute;font-size:7px;font-weight:700;padding:2px 6px;border-radius:3px}
.stars{position:absolute;left:286px;top:48px;display:flex;gap:4px}
.slide h3{position:absolute;left:286px;top:76px;width:410px;color:#fff;font-size:24px;line-height:1.3;font-weight:700}
.slide .q{position:absolute;left:286px;top:162px;width:400px;color:#dfeaff;font-size:12px;line-height:1.7}
.slide .au{position:absolute;left:286px;top:244px;color:#fff;font-weight:700;font-size:14px}
.team-head{left:139px;top:3160px}
.team-head h2{font-size:40px;font-weight:700;line-height:1.25;margin-top:12px}
.tm{top:3362px;height:298px;background:linear-gradient(180deg,#e3eefc,#f5f9ff);border-radius:12px}
.tm .ph{position:absolute;left:0;right:0;top:0;height:220px;border-radius:12px 12px 0 0;background:linear-gradient(180deg,#dbe8fa,#b8cfee)}
.tm .lbl{position:absolute;left:12px;right:12px;bottom:14px;height:58px;background:#fff;border-radius:8px;text-align:center;padding-top:12px}
.tm .lbl b{display:block;font-size:16px}
.tm .lbl small{font-size:9px;color:var(--muted)}
.tm .plus{position:absolute;left:30px;top:192px;width:26px;height:26px;border-radius:50%;background:var(--blue);border:2px solid #fff;color:#fff;font-size:16px;line-height:21px;text-align:center}
.tm.active{top:3340px;height:322px;background:#fff;box-shadow:0 14px 34px rgba(14,40,110,.15);z-index:2}
.tm.active .lbl{background:var(--blue);text-align:left;padding:14px 16px;color:#fff}
.tm.active .lbl small{color:#dbe7ff}
.tm.active .plus{background:var(--green)}
.soc{position:absolute;top:22px;width:24px;height:24px;border-radius:50%;background:rgba(255,255,255,.25)}
.sched{left:191px;top:3921px;width:816px;height:496px;border-radius:30px;background:linear-gradient(135deg,#1fbf9b,#11977c);padding:0}
.fl{position:absolute;color:#dff7f0;font-size:10px}
.fi-in{position:absolute;height:44px;background:#fff;border-radius:6px;font-size:11px;color:var(--navy);display:flex;align-items:center;padding:0 14px;justify-content:space-between}
.chk{width:14px;height:14px;border-radius:50%;background:var(--blue)}
.ring{width:14px;height:14px;border-radius:50%;border:1.5px solid #aab4c6}
.confirm{position:absolute;left:74px;top:379px;width:206px;height:42px;background:var(--blue);border-radius:6px;color:#fff;font-size:11px;display:flex;align-items:center;justify-content:center}
.foot{left:0;top:4460px;width:1200px;height:454px;background:linear-gradient(180deg,#ffffff,#eef4fe)}
.fcol h5{font-size:14px;font-weight:700;margin-bottom:22px}
.fc-row{display:flex;gap:12px;font-size:10px;color:var(--text);margin-bottom:18px;line-height:1.5}
.fc-row b{color:var(--navy);font-size:15px}
.fc-row .mail{color:var(--green);font-weight:600}
.links{list-style:none;font-size:10.5px;color:var(--text)}
.links li{margin-bottom:20px}
.links li::before{content:"» ";color:var(--blue)}
.map{width:180px;height:145px;border:3px solid var(--blue);border-radius:4px;background:linear-gradient(135deg,#eef0f2,#dfe6ec)}
.copy{left:0;top:4862px;width:1200px;border-top:1px solid var(--line);padding-top:14px;text-align:center;font-size:9px;color:var(--text)}
.sq-soc{width:30px;height:30px;border-radius:6px;background:var(--green)}
</style>
</head>
<body>

<!-- Hero -->
<div class="abs hero-bg"></div>
<svg class="abs hero-wave" viewBox="0 0 1200 190" preserveAspectRatio="none"><path d="M0 190 C120 70 330 50 600 50 C860 50 1060 80 1200 140 L1200 190 Z" fill="#fff"/></svg>

<div class="abs topbar">
  <div class="item"><span class="ic"><svg width="10" height="10" viewBox="0 0 24 24"><path d="M12 2a7 7 0 0 0-7 7c0 5 7 13 7 13s7-8 7-13a7 7 0 0 0-7-7zm0 9.5A2.5 2.5 0 1 1 12 6.5a2.5 2.5 0 0 1 0 5z" fill="#1c6ff0"/></svg></span>Location: <b>&nbsp;48 Maplecrest Lane, Fairview</b></div>
  <div class="item"><span class="ic"><svg width="10" height="10" viewBox="0 0 24 24"><path d="M6.6 10.8a15 15 0 0 0 6.6 6.6l2.2-2.2a1 1 0 0 1 1-.25 11.4 11.4 0 0 0 3.6.57 1 1 0 0 1 1 1V20a1 1 0 0 1-1 1A17 17 0 0 1 3 4a1 1 0 0 1 1-1h3.5a1 1 0 0 1 1 1c0 1.250.2 2.450.57 3.6a1 1 0 0 1-.25 1z" fill="#1c6ff0"/></svg></span>Call Us: <b>&nbsp;(555) 014-2290</b></div>
  <div class="follow">Follow Us: <span class="dot-soc"></span><span class="dot-soc"></span></div>
</div>

<nav class="abs nav">
  <div class="brand"><span class="sq"></span>Maplecrest Dentistry</div>
  <ul><li class="active">HOME</li><li>ABOUT</li><li>SERVICES</li><li>PROCEDURES</li><li>CONTACT</li></ul>
  <a class="btn btn-green" style="font-size:10px;width:132px">LET'S TALK <span class="bi"><svg width="12" height="12" viewBox="0 0 24 24"><path d="M7 17 17 7M9 7h8v8" stroke="#1fbf9b" stroke-width="3" fill="none"/></svg></span></a>
</nav>

<div class="abs pill">24/7 Service Available</div>
<h1 class="abs hero-h1"><span class="l1">Gentle Care for</span><span class="l2">BRIGHT SMILES</span></h1>
<p class="abs hero-p">Experience top-quality dental care focused on your smile's health &amp; beauty. Trust us to create a brighter, healthier tomorrow.</p>
<a class="abs btn btn-white" style="left:93px;top:450px;width:218px">Schedule Appointment <span class="bi"><svg width="12" height="12" viewBox="0 0 24 24"><path d="M7 17 17 7M9 7h8v8" stroke="#fff" stroke-width="3" fill="none"/></svg></span></a>

<div class="abs hero-img" role="img" aria-label="Patient smiling in the dental chair during a check-up"></div>
<div class="abs badge-9k"><span class="av" role="img" aria-label="Patient portrait"></span><span class="av" role="img" aria-label="Patient portrait"></span><span class="k9">9K+</span></div>
<div class="abs award" role="img" aria-label="Award badge"></div>

<div class="abs info-card">
  <div class="info"><span class="ib"><svg width="20" height="20" viewBox="0 0 24 24"><path d="M6.6 10.8a15 15 0 0 0 6.6 6.6l2.2-2.2a1 1 0 0 1 1-.25 11.4 11.4 0 0 0 3.6.57 1 1 0 0 1 1 1V20a1 1 0 0 1-1 1A17 17 0 0 1 3 4a1 1 0 0 1 1-1h3.5a1 1 0 0 1 1 1c0 1.250.2 2.450.57 3.6a1 1 0 0 1-.25 1z" fill="#fff"/></svg></span><div><small>Need a Dental Services?</small><strong>(555) 014-2290</strong></div></div>
  <div class="info"><span class="ib"><svg width="20" height="20" viewBox="0 0 24 24"><circle cx="12" cy="12" r="9" fill="#fff"/><path d="M12 7v5l3 2" stroke="#1fbf9b" stroke-width="2" fill="none"/></svg></span><div><small>Opening Hours</small><span>Mon to Sat <b>9:00AM</b> to <b>6:00PM</b></span></div></div>
  <div class="info"><span class="ib"><svg width="20" height="20" viewBox="0 0 24 24"><path d="M12 2a7 7 0 0 0-7 7c0 5 7 13 7 13s7-8 7-13a7 7 0 0 0-7-7zm0 9.5A2.5 2.5 0 1 1 12 6.5a2.5 2.5 0 0 1 0 5z" fill="#fff"/></svg></span><div><small>Our Location</small><span>48 Willow Meadow Lane<br>Fairview, CA 90210</span></div></div>
</div>

<!-- About -->
<div class="abs about-glow"></div>
<div class="abs about-img" role="img" aria-label="Smiling patient giving a thumbs up in the dental chair"></div>
<div class="abs tooth" style="left:395px;top:868px;width:52px;height:70px" role="img" aria-label="Tooth illustration"></div>
<div class="abs about-tag"><div class="nm">Maplecrest Dentistry</div><div class="row"><span class="av"></span><span class="av"></span><span class="av"></span><span style="margin-left:16px">09K + Happy Customers</span></div></div>
<div class="abs about-text">
  <h2>We provide Gentle, Modern Dental care in a calm, Welcoming environment for Every Smile.</h2>
  <p class="sub">Need a Dental Services? We take care of You.</p>
  <a class="btn btn-blue" style="width:220px">Schedule Appointment <span class="bi"><svg width="12" height="12" viewBox="0 0 24 24"><path d="M7 17 17 7M9 7h8v8" stroke="#1c6ff0" stroke-width="3" fill="none"/></svg></span></a>
</div>
<div class="abs tooth" style="left:1160px;top:1210px;width:70px;height:110px" role="img" aria-label="Tooth illustration"></div>

<!-- Services -->
<div class="abs sec-head" style="top:1297px"><span class="leaf" role="img" aria-label="Leaf ornament"></span><h2>Turning Your Smile Into<br><span class="g">An Experience</span></h2></div>

<div class="abs svc" style="left:88px"><div class="im" style="background:linear-gradient(135deg,#bfe9e6,#7fd2cc)" role="img" aria-label="Woman pointing at her bright smile"></div><span class="ico"><svg width="22" height="22" viewBox="0 0 24 24"><path d="M7 3c-3 0-4 3-3 6l2 11c.3 1 1.7 1 2 0l1.5-6h5L16 20c.3 1 1.7 1 2 0l2-11c1-3 0-6-3-6-2 0-3 1-5 1S9 3 7 3z" fill="#fff"/></svg></span><h3>Cosmetic Dentistry</h3><p>Enhance your smile with whitening, veneers, and natural-looking restorations.</p><span class="arr"><svg width="16" height="16" viewBox="0 0 24 24"><path d="M7 17 17 7M9 7h8v8" stroke="#1fbf9b" stroke-width="2.5" fill="none"/></svg></span></div>
<div class="abs svc" style="left:351px"><div class="im" style="background:linear-gradient(135deg,#d9c3b6,#6d8fc4)" role="img" aria-label="Dentist matching tooth shades for implants"></div><span class="ico b"><svg width="22" height="22" viewBox="0 0 24 24"><path d="M7 3c-3 0-4 3-3 6l2 11c.3 1 1.7 1 2 0l1.5-6h5L16 20c.3 1 1.7 1 2 0l2-11c1-3 0-6-3-6-2 0-3 1-5 1S9 3 7 3z" fill="#fff"/></svg></span><h3>Implants</h3><p>Permanent, comfortable solutions to restore missing teeth and confidence.</p><span class="arr on"><svg width="16" height="16" viewBox="0 0 24 24"><path d="M7 17 17 7M9 7h8v8" stroke="#fff" stroke-width="2.5" fill="none"/></svg></span></div>
<div class="abs svc" style="left:612px"><div class="im" style="background:linear-gradient(135deg,#dfe6ef,#8fb0d8)" role="img" aria-label="Dentist examining a patient during a cleaning"></div><span class="ico"><svg width="22" height="22" viewBox="0 0 24 24"><path d="M7 3c-3 0-4 3-3 6l2 11c.3 1 1.7 1 2 0l1.5-6h5L16 20c.3 1 1.7 1 2 0l2-11c1-3 0-6-3-6-2 0-3 1-5 1S9 3 7 3z" fill="#fff"/></svg></span><h3>Dental Hygiene</h3><p>Preventive cleanings and checkups to keep your mouth healthy and fresh.</p><span class="arr"><svg width="16" height="16" viewBox="0 0 24 24"><path d="M7 17 17 7M9 7h8v8" stroke="#1fbf9b" stroke-width="2.5" fill="none"/></svg></span></div>
<div class="abs svc" style="left:876px"><div class="im" style="background:linear-gradient(135deg,#9bb7df,#2f5ea8)" role="img" aria-label="Dental team treating an urgent case"></div><span class="ico"><svg width="22" height="22" viewBox="0 0 24 24"><path d="M6 18v-6a6 6 0 0 1 12 0v6zM4 20h16M12 2v3" stroke="#fff" stroke-width="2" fill="none"/></svg></span><h3>Emergency Services</h3><p>Prompt care for pain, injuries, or unexpected dental issues—when you need it most.</p><span class="arr"><svg width="16" height="16" viewBox="0 0 24 24"><path d="M7 17 17 7M9 7h8v8" stroke="#1fbf9b" stroke-width="2.5" fill="none"/></svg></span></div>
<div class="abs dots" style="top:1857px"><span class="c"></span><span class="p"></span></div>

<!-- Why choose -->
<div class="abs why-head"><span class="leaf" role="img" aria-label="Leaf ornament"></span><h2><span class="g">Why Choose</span><br>Maplecrest Dentistry?</h2></div>
<a class="abs btn btn-blue" style="left:840px;top:2054px;width:220px">Schedule Appointment <span class="bi"><svg width="12" height="12" viewBox="0 0 24 24"><path d="M7 17 17 7M9 7h8v8" stroke="#1c6ff0" stroke-width="3" fill="none"/></svg></span></a>
<div class="abs why-b" role="img" aria-label="Dentist treating a smiling patient"></div>
<div class="abs why-a" role="img" aria-label="Close-up of a bright white smile"></div>
<div class="abs tooth" style="left:318px;top:2365px;width:62px;height:90px" role="img" aria-label="Tooth illustration"></div>

<div class="abs feat" style="top:2162px"><span class="fi"><svg width="30" height="30" viewBox="0 0 24 24"><circle cx="12" cy="7" r="3" fill="#1fbf9b"/><path d="M5 21c0-4 3-7 7-7s7 3 7 7z" fill="#1fbf9b"/></svg></span><div><h4>Comfort-First Experience</h4><p>from soothing colors and gentle lighting to a warm, welcoming team that treats you like family.</p></div></div>
<div class="abs feat" style="top:2262px"><span class="fi b"><svg width="30" height="30" viewBox="0 0 24 24"><rect x="3" y="4" width="18" height="12" rx="1.5" stroke="#fff" stroke-width="1.8" fill="none"/><path d="M8 20h8M12 16v4" stroke="#fff" stroke-width="1.8"/></svg></span><div><h4>Modern Dental Technology</h4><p>We use techniques to ensure fast, precise, and pain-free treatments that help you feel confident and cared for.</p></div></div>
<div class="abs feat" style="top:2362px"><span class="fi"><svg width="30" height="30" viewBox="0 0 24 24"><circle cx="10" cy="12" r="7" stroke="#1fbf9b" stroke-width="2" fill="none"/><circle cx="14" cy="12" r="7" fill="#1fbf9b" opacity=".5"/></svg></span><div><h4>Patient Education &amp; Transparency</h4><p>we explain every step and provide honest, clear communication.</p></div></div>

<!-- Stories -->
<div class="abs sec-head" style="top:2565px"><span class="leaf" role="img" aria-label="Leaf ornament"></span><h2>Real Stories from <span class="g">Happy Smiles.</span></h2></div>
<div class="abs slider">
  <div class="slide side" style="left:-530px;width:721px">
    <div class="ba" role="img" aria-label="Before and after smile comparison"></div>
    <h3>The team at Maplecrest Dentistry made me feel so welcome.</h3>
    <p class="q">"Lorem ipsum dolor sit amet, consectetuer adipiscing elit, sed diam nonummy nibh euismod tincidunt ut laoreet dolore magna aliquam erat volutpat. Ut wisi enim ad minim."</p>
  </div>
  <div class="slide main">
    <div class="ba" role="img" aria-label="Before and after teeth whitening comparison"><i></i><span class="tagsm" style="left:10px;top:10px;background:#fff;color:var(--navy)">BEFORE</span><span class="tagsm" style="left:196px;top:276px;background:var(--green);color:#fff">AFTER</span></div>
    <div class="stars"><svg width="90" height="14" viewBox="0 0 90 14"><g fill="#ffd43b"><path id="st" d="M7 0l2 4.6 5 .4-3.8 3.3L11.3 13 7 10.4 2.7 13l1.1-4.7L0 5l5-.4z"/><use href="#st" x="19"/><use href="#st" x="38"/><use href="#st" x="57"/><use href="#st" x="76"/></g></svg></div>
    <h3>The team at Maplecrest Dentistry made me feel so welcome.</h3>
    <p class="q">"Lorem ipsum dolor sit amet, consectetuer adipiscing elit, sed diam nonummy nibh euismod tincidunt ut laoreet dolore magna aliquam erat volutpat. Ut wisi enim ad minim."</p>
    <p class="au">-Clara W.</p>
  </div>
  <div class="slide" style="left:973px;width:260px;background:#fff;border:3px solid var(--blue)"><div class="ba" style="left:3px;top:3px;width:248px;height:296px;background:linear-gradient(90deg,#e6d2c8,#f4ece8)" role="img" aria-label="Before and after smile comparison"><span class="tagsm" style="left:10px;top:276px;background:var(--green);color:#fff">AFTER</span></div></div>
</div>
<div class="abs dots" style="top:3051px"><span class="c"></span><span class="p"></span></div>

<!-- Team -->
<div class="abs team-head"><span class="leaf" role="img" aria-label="Leaf ornament"></span><h2>Meet the Maplecrest<br><span class="g">Dentistry Team</span></h2></div>
<a class="abs btn btn-blue" style="left:840px;top:3224px;width:220px">Schedule Appointment <span class="bi"><svg width="12" height="12" viewBox="0 0 24 24"><path d="M7 17 17 7M9 7h8v8" stroke="#1c6ff0" stroke-width="3" fill="none"/></svg></span></a>

<div class="abs tm" style="left:139px;width:245px"><div class="ph" role="img" aria-label="Portrait of the lead dentist"></div><span class="plus">+</span><div class="lbl"><b>Dr. Emily Hart</b><small>Lead Dentist</small></div></div>
<div class="abs tm" style="left:395px;width:246px"><div class="ph" role="img" aria-label="Portrait of the dental hygienist"></div><span class="plus">+</span><div class="lbl"><b>Owen Park, RDH</b><small>Dental Hygienist</small></div></div>
<div class="abs tm" style="left:814px;width:245px"><div class="ph" role="img" aria-label="Portrait of the dental hygienist"></div><div class="lbl" style="text-align:left;padding-left:60px"><b>Owen Park, RDH</b><small>Dental Hygienist</small></div></div>
<div class="abs tm active" style="left:598px;width:263px"><div class="ph" style="top:-50px;height:270px;background:linear-gradient(180deg,rgba(255,255,255,0),#dbe8fa)" role="img" aria-label="Portrait of the office manager"></div><span class="plus">−</span><div class="lbl"><b>Lena Ortiz</b><small>Office Manager</small><span class="soc" style="right:42px"></span><span class="soc" style="right:12px"></span></div></div>

<!-- Schedule -->
<div class="abs sec-head" style="top:3795px"><span class="leaf" role="img" aria-label="Leaf ornament"></span><h2>Schedule <span class="g">Appointment</span></h2></div>
<div class="abs tooth" style="left:160px;top:4150px;width:52px;height:70px" role="img" aria-label="Tooth illustration"></div>
<div class="abs sched">
  <span class="fl" style="left:80px;top:58px">First Name*</span>
  <div class="fi-in" style="left:74px;top:77px;width:328px">Owen Park, RDH <span class="chk"></span></div>
  <span class="fl" style="left:425px;top:58px">Last Name*</span>
  <div class="fi-in" style="left:419px;top:77px;width:326px">Owen Park, RDH</div>
  <span class="fl" style="left:80px;top:146px">Doctor</span>
  <div class="fi-in" style="left:74px;top:164px;width:328px">Dr. Emily Hart <span class="ring"></span></div>
  <span class="fl" style="left:425px;top:146px">Appoinment Date</span>
  <div class="fi-in" style="left:419px;top:164px;width:326px">Monday, 6th April, 25 <span class="ring"></span></div>
  <span class="fl" style="left:80px;top:233px">Available Hours</span>
  <div class="fi-in" style="left:74px;top:251px;width:152px">9:00 AM</div>
  <div class="fi-in" style="left:249px;top:251px;width:152px">10:00 AM <span class="chk"></span></div>
  <div class="fi-in" style="left:419px;top:251px;width:152px">11:00 AM</div>
  <div class="fi-in" style="left:592px;top:251px;width:152px">1:00 PM</div>
  <div class="fi-in" style="left:74px;top:314px;width:152px">2:00 PM</div>
  <div class="fi-in" style="left:249px;top:314px;width:152px">3:00 PM</div>
  <div class="fi-in" style="left:419px;top:314px;width:152px">4:00 PM</div>
  <div class="fi-in" style="left:592px;top:314px;width:152px">5:00 PM</div>
  <div class="confirm">Confirm&nbsp;<b>Date And Time</b></div>
</div>
<div class="abs tooth" style="left:975px;top:3920px;width:60px;height:80px" role="img" aria-label="Tooth illustration"></div>

<!-- Footer -->
<footer class="abs foot">
  <div class="abs" style="left:139px;top:50px">
    <div class="brand" style="font-size:20px"><span class="sq"></span>Maplecrest Dentistry</div>
    <div style="display:flex;gap:10px;margin-top:26px;padding-left:52px"><span class="sq-soc"></span><span class="sq-soc"></span></div>
  </div>
  <div class="abs fcol" style="left:399px;top:50px;width:240px">
    <h5>CONTACT US</h5>
    <div class="fc-row"><svg width="16" height="16" viewBox="0 0 24 24"><path d="M12 2a7 7 0 0 0-7 7c0 5 7 13 7 13s7-8 7-13a7 7 0 0 0-7-7zm0 9.5A2.5 2.5 0 1 1 12 6.5a2.5 2.5 0 0 1 0 5z" fill="#1c6ff0"/></svg><div>Address<br>48 Willow Meadow Lane, Fairview,<br>CA 90210</div></div>
    <div class="fc-row"><svg width="16" height="16" viewBox="0 0 24 24"><path d="M6.6 10.8a15 15 0 0 0 6.6 6.6l2.2-2.2a1 1 0 0 1 1-.25 11.4 11.4 0 0 0 3.6.57 1 1 0 0 1 1 1V20a1 1 0 0 1-1 1A17 17 0 0 1 3 4a1 1 0 0 1 1-1h3.5a1 1 0 0 1 1 1c0 1.250.2 2.450.57 3.6a1 1 0 0 1-.25 1z" fill="#1c6ff0"/></svg><div>Call us<br><b>(555) 014-2290</b></div></div>
    <div class="fc-row"><svg width="16" height="16" viewBox="0 0 24 24"><rect x="2" y="5" width="20" height="14" rx="2" fill="#1c6ff0"/><path d="M2 7l10 6 10-6" stroke="#fff" stroke-width="1.5" fill="none"/></svg><div>Email us<br><span class="mail">hello@maplecrestdentistry.com</span></div></div>
    <div class="fc-row"><svg width="16" height="16" viewBox="0 0 24 24"><circle cx="12" cy="12" r="9" stroke="#1c6ff0" stroke-width="2" fill="none"/><path d="M12 7v5l3 2" stroke="#1c6ff0" stroke-width="2" fill="none"/></svg><div>Business Hours<br>Monday – Friday: <b style="font-size:10px">8:00 AM – 5:00 PM</b><br>Saturday: <b style="font-size:10px">9:00 AM – 2:00 PM</b><br>Sunday: <b style="font-size:10px">Closed</b></div></div>
  </div>
  <div class="abs fcol" style="left:714px;top:50px">
    <h5>LINKS</h5>
    <ul class="links"><li>Home</li><li>About us</li><li>Services</li><li>Procedures</li><li>Testimonials</li><li>Why Choose Us</li><li>Contact us</li></ul>
  </div>
  <div class="abs fcol" style="left:880px;top:50px">
    <h5>OUR LOCATION</h5>
    <div class="map" role="img" aria-label="Map showing the clinic location"></div>
  </div>
</footer>
<div class="abs copy">©2025 MAPLECREST DENTISTRY. ALL RIGHTS RESERVED.</div>

</body>
</html>
```